Zielgruppe
Planung und Realisierung von individuellen und wertbeständigen Kamin- und Ofenlösungen, sowie Fliesen- und Baddesign.
Aufgabenstellung
Wir benötigen ein möglichst schlichtes Design für Visitenkarten, bzw. Briefpapier. Für die Visitenkarten gerne auch Vorschläge mit Prägung, Ausstanzung oder mit Heißfolie. Auch Klappkarten wären denkbar. Das Design soll "das gewisse Etwas haben" und nicht zu verspielt sein.
Die Visitenkarten sind für die Firma KARMU, das Logo von der Ausstellung "talgrund" soll dezent mit eingebunden werden (bei dem Briefpapier z.B. in der Fußzeile". Die farbliche Gestaltung sollte sich an den Farben des Logos orientieren.
Schriftart für Texte: Century Gothic
Schriftfarbe: RAL 7016
Nur eine Idee: Ich könnte mir auch gut vorstellen, dass die Visitenkarte aus einer Zündholzverpackung (wenn dann aber eine besondere mit nur einem Zündholz oder einem besonders breiten) besteht: http://lindoraversand.de/produkte_briefchen.php

```html
<!DOCTYPE html>
<html lang="de">
<head>
<meta charset="utf-8">
<title>KARMU Geschäftsausstattung</title>
<link rel="stylesheet" href="https://fonts.googleapis.com/css2?family=Questrial&display=swap">
<style>
  :root {
    --board: #be9960;
    --paper: #ffffff;
    --anthracite: #142830;
    --flame: #f47a12;
    --shadow: rgba(40, 25, 5, 0.55);
  }
  * { margin: 0; padding: 0; box-sizing: border-box; }
  html, body { width: 1200px; height: 1120px; overflow: hidden; }
  body {
    background: var(--board);
    font-family: "Questrial", "Century Gothic", sans-serif;
    color: var(--anthracite);
    position: relative;
  }
  .sheet, .card {
    position: absolute;
    background: var(--paper);
    box-shadow: 14px 16px 18px var(--shadow);
    overflow: hidden;
  }

  /* Letterhead */
  .letterhead { left: 398px; top: 46px; width: 728px; height: 1029px; }
  .brand { position: absolute; white-space: nowrap; }
  .brand-name { font-size: 44px; line-height: 1; letter-spacing: 1px; display: flex; align-items: center; gap: 6px; }
  .brand-dot { width: 9px; height: 9px; border-radius: 50%; background: var(--flame); display: inline-block; }
  .brand-tagline { font-size: 14px; margin-top: 4px; }
  .letterhead .brand { right: 30px; top: 34px; text-align: right; }
  .info-block { position: absolute; left: 548px; top: 124px; width: 148px; }
  .info-rule { height: 6px; background: var(--anthracite); }
  .info-lines { padding: 9px 0 6px; font-size: 13px; line-height: 17px; letter-spacing: 0.5px; white-space: nowrap; }
  .info-lines .row { display: flex; justify-content: space-between; }
  .info-lines .address { letter-spacing: 1px; }
  .info-lines .web { font-size: 10.8px; line-height: 14px; letter-spacing: 0.6px; margin-top: 4px; }
  .info-lines .partner { text-align: right; font-size: 11px; letter-spacing: 0; margin-top: 4px; }
  .sender-line { position: absolute; left: 88px; top: 185px; font-size: 8.5px; letter-spacing: 0.6px; display: flex; align-items: center; gap: 4px; white-space: nowrap; }
  .sender-line .mark { width: 5px; height: 5px; border-radius: 50%; background: var(--flame); }
  .fold-mark { position: absolute; width: 4px; height: 4px; background: var(--anthracite); }
  .edge-mark { position: absolute; left: 0; width: 0; height: 0; border-top: 6px solid transparent; border-bottom: 6px solid transparent; border-left: 6px solid var(--anthracite); }
  .legal-footer {
    position: absolute; left: 0; bottom: 0; width: 100%; height: 88px;
    background: var(--anthracite); color: #e8ecee;
    font-size: 8.3px; line-height: 12.2px; white-space: nowrap;
  }
  .legal-footer .company { position: absolute; left: 70px; top: 13px; }
  .legal-footer .bank { position: absolute; right: 34px; top: 13px; text-align: right; }
  .legal-footer .mark { position: absolute; left: 22px; top: 32px; width: 22px; height: 22px; border-radius: 50%; background: var(--flame); }

  /* Business cards */
  .card { width: 295px; height: 190px; }
  .card-front { left: 53px; top: 381px; }
  .card-back { left: 53px; top: 610px; background: var(--anthracite); }
  .card-front .brand { left: 9px; top: 11px; }
  .card-front .brand-name { font-size: 30px; }
  .card-front .brand-dot { width: 7px; height: 7px; }
  .card-front .brand-tagline { font-size: 10px; margin-top: 2px; }
  .holder { position: absolute; right: 91px; top: 78px; text-align: right; white-space: nowrap; }
  .holder-name { font-size: 16px; line-height: 1; }
  .holder-role { font-size: 6px; color: var(--flame); letter-spacing: 0.3px; }
  .contact-band {
    position: absolute; left: 0; top: 122px; width: 100%; height: 68px;
    background: var(--anthracite); color: #e8ecee; white-space: nowrap;
  }
  .contact-band .address { position: absolute; left: 9px; top: 6px; font-size: 9.5px; line-height: 12px; letter-spacing: 1px; }
  .contact-band .phones { position: absolute; left: 9px; top: 31px; font-size: 7.5px; line-height: 11px; }
  .contact-band .mail { position: absolute; left: 9px; top: 55px; font-size: 7px; letter-spacing: 0.8px; }
  .contact-band .web { position: absolute; right: 5px; top: 55px; font-size: 7px; letter-spacing: 0.8px; }
  .card-accent { position: absolute; right: 26px; top: 44px; width: 40px; height: 40px; border-radius: 50%; background: var(--flame); }
  .card-back .card-accent { left: 124px; top: 72px; right: auto; width: 46px; height: 46px; }
  .card-back .partner { position: absolute; right: 9px; bottom: 10px; color: #ffffff; font-size: 11px; }
</style>
</head>
<body>

  <section class="card card-front" aria-label="Visitenkarte Vorderseite">
    <div class="brand">
      <div class="brand-name">KARMU <span class="brand-dot"></span></div>
      <div class="brand-tagline">kamine · öfen · fliesen</div>
    </div>
    <span class="card-accent"></span>
    <div class="holder">
      <div class="holder-name">Jonas Karmu</div>
      <div class="holder-role">Geschäftsführer</div>
    </div>
    <div class="contact-band">
      <div class="address">Am Lindenhang 8b<br>34512&nbsp;&nbsp;&nbsp;&nbsp;Talheim</div>
      <div class="phones">fon:&nbsp;&nbsp;&nbsp;05412 / 38 71 40<br>fax:&nbsp;&nbsp;&nbsp;05412 / 38 71 48</div>
      <div class="mail">info@karmu-talheim.de</div>
      <div class="web">www.karmu-talheim.de</div>
    </div>
  </section>

  <section class="card card-back" aria-label="Visitenkarte Rückseite">
    <span class="card-accent"></span>
    <div class="partner">talgrund</div>
  </section>

  <section class="sheet letterhead" aria-label="Briefpapier">
    <div class="brand">
      <div class="brand-name">KARMU <span class="brand-dot"></span></div>
      <div class="brand-tagline">kamine · öfen · fliesen</div>
    </div>

    <div class="info-block">
      <div class="info-rule"></div>
      <div class="info-lines">
        <div class="row address"><span>Am Lindenhang 8b</span></div>
        <div class="row address"><span>34512</span><span>Talheim</span></div>
        <div class="row"><span>fon:</span><span>05412 / 38 71 40</span></div>
        <div class="row"><span>fax:</span><span>05412 / 38 71 48</span></div>
        <div class="web">info@karmu-talheim.de<br>www.karmu-talheim.de</div>
        <div class="partner">talgrund</div>
      </div>
      <div class="info-rule"></div>
    </div>

    <div class="sender-line"><span class="mark"></span>Karmu GmbH &nbsp;|&nbsp; Am Lindenhang 8b &nbsp;|&nbsp; 34512 Talheim</div>

    <span class="fold-mark" style="left:70px; top:331px;"></span>
    <span class="fold-mark" style="left:363px; top:331px;"></span>
    <span class="edge-mark" style="top:358px;"></span>
    <span class="edge-mark" style="top:721px;"></span>

    <footer class="legal-footer">
      <span class="mark"></span>
      <div class="company">
        Karmu GmbH<br>
        Vertretungsberechtigter Geschäftsführer: Jonas Karmu<br>
        Registergericht: Amtsgericht Talheim<br>
        Handelsregisternummer: HRB 412<br>
        Zuständige Kammer:<br>
        Handwerkskammer Nordtal, Brunnenplatz 4, 34120 Nordtal
      </div>
      <div class="bank">
        Bankverbindung:<br>
        Sparkasse Talheim<br>
        Konto-Nr.: 204 718<br>
        Blz: 512 300 44<br>
        IBAN: DE48 5123 0044 0000 2047 18<br>
        BIC: TALHDE21XXX
      </div>
    </footer>
  </section>

</body>
</html>
```